Distillery looking for bottle label

We are looking for a label design for our bottles that will accurately reflect who we are and what we believe. The winning design will be challenged to create a bad ass label for our project! The design will be for our entire line of distilled products. The winning designer will also be contracted to do one-on-one design work for each label. We make white rum, spiced rum, vodka, sugar shine and whiskey. The label needs to keep the same design elements throughout the design, but also be able to differentiate each product.

Target Market(s)

men and women that enjoy distilled spirits.

Logo Text

Hollow Creek

Colors

Designer to choose colors to be used in the design.

Requirements
Must have
• Our project needs to portray our why.
• Our name was born out of the determination to create a company that speaks to the American Spirit. Remain unbound, unrestrained, uninhibited and free from limitations. Our intention is to create custom, handcrafted spirits worthy of those standards and focus on those that believe in living free.
• Our spirits are always made from the finest ingredients and hand crafted to the highest standard. The winning label can be a rum or vodka. The winning designer will receive additional projects to complete the line up. The label can be just a front label or front and back. There will need to be room for the barcode, government warning and distilled and bottled by Hollow Creek, St. Louis, MO
Nice to have
• We are located in a speed shop. One of the attached photos are of the shop truck door. We would like the same font, vintage feel, and/or coloring to coordinate with the shop truck.
• We have included a couple examples of labels we like. We do not want to copy any, but our favorite of the group is Bramble Row. We also like how Quill Ferments, Halvik and Corvel Ridge Distillery show the same artwork across the entire lineup. We want vintage, industrial type of look.
Should not have
• While we are in a speed shop, we do not want to be solely car focused. We want a very loose tie to the shop truck, but not the truck on the label.
• We do not like modern look. We want a vintage, industrial type of label.

```html
<!DOCTYPE html>
<html lang="en">
<head>
<meta charset="utf-8">
<title>Hollow Creek Rum Label</title>
<link rel="stylesheet" href="https://fonts.googleapis.com/css2?family=Kaushan+Script&family=Quicksand:wght@400;500;600&display=swap">
<style>
  :root {
    --backdrop: #dcdcda;
    --paper: #ededeb;
    --ink: #3b3b3b;
    --ink-soft: #5a5a5a;
    --ornament: #8a8a88;
    --ribbon-text: #e6e6e4;
  }
  * { margin: 0; padding: 0; box-sizing: border-box; }
  html, body { width: 1200px; height: 1000px; overflow: hidden; }
  body {
    background: var(--backdrop);
    display: flex;
    align-items: center;
    justify-content: center;
  }
  .label {
    position: relative;
    width: 690px;
    height: 1000px;
    background: var(--paper);
    color: var(--ink);
    font-family: "Quicksand", sans-serif;
    overflow: hidden;
  }
  .label > * { position: absolute; }
  .corner-ornament {
    width: 68px;
    height: 48px;
    background: var(--ornament);
    opacity: 0.35;
  }
  .corner-ornament--tl { left: 45px; top: 52px; }
  .corner-ornament--tr { left: 540px; top: 58px; }
  .corner-ornament--bl { left: 35px; top: 788px; }
  .corner-ornament--br { left: 582px; top: 932px; }
  .brand-name {
    left: 0; right: 0; top: 92px;
    text-align: center;
    font-weight: 600;
    font-size: 46px;
    letter-spacing: 2px;
    color: var(--ink);
  }
  .location {
    left: 0; right: 0; top: 225px;
    text-align: center;
    font-size: 20px;
    font-weight: 500;
    letter-spacing: 1px;
    color: var(--ink-soft);
  }
  .divider { left: 0; width: 690px; height: 12px; }
  .divider--upper { top: 276px; }
  .divider--lower { top: 356px; }
  .style-line {
    left: 0; right: 0; top: 296px;
    text-align: center;
    font-family: "Kaushan Script", cursive;
    font-size: 38px;
    line-height: 50px;
    color: var(--ink);
  }
  .product-frame { left: 0; top: 430px; width: 690px; height: 130px; }
  .product-name {
    left: 0; right: 0; top: 462px;
    text-align: center;
    font-size: 54px;
    font-weight: 500;
    letter-spacing: 2px;
  }
  .spec { font-size: 22px; font-weight: 500; color: var(--ink); text-align: center; width: 160px; }
  .spec--strength { left: 175px; top: 613px; }
  .spec--proof { left: 352px; top: 613px; }
  .spec--volume { left: 175px; top: 653px; }
  .spec--abv { left: 352px; top: 653px; }
  .spec-rules { left: 0; top: 630px; width: 690px; height: 24px; }
  .est-ribbon { left: 222px; top: 722px; width: 250px; height: 74px; }
  .tagline {
    left: 60px; right: 60px; top: 850px;
    text-align: center;
    font-family: "Kaushan Script", cursive;
    font-size: 22px;
    line-height: 36px;
    white-space: nowrap;
    color: var(--ink-soft);
  }
</style>
</head>
<body>
  <main class="label">
    <div class="corner-ornament corner-ornament--tl" role="img" aria-label="Decorative corner flourish"></div>
    <div class="corner-ornament corner-ornament--tr" role="img" aria-label="Decorative corner flourish"></div>
    <div class="corner-ornament corner-ornament--bl" role="img" aria-label="Decorative corner flourish"></div>
    <div class="corner-ornament corner-ornament--br" role="img" aria-label="Decorative corner flourish"></div>

    <h1 class="brand-name">Hollow Creek</h1>
    <p class="location">ASHFORD BEND, MISSOURY</p>

    <svg class="divider divider--upper" viewBox="0 0 690 12" aria-hidden="true">
      <line x1="178" y1="6" x2="496" y2="6" stroke="#3b3b3b" stroke-width="2"/>
      <circle cx="337" cy="6" r="4" fill="#3b3b3b"/>
    </svg>
    <p class="style-line">Distilled</p>
    <svg class="divider divider--lower" viewBox="0 0 690 12" aria-hidden="true">
      <line x1="178" y1="6" x2="496" y2="6" stroke="#3b3b3b" stroke-width="2"/>
      <circle cx="337" cy="6" r="4" fill="#3b3b3b"/>
    </svg>

    <svg class="product-frame" viewBox="0 0 690 130" aria-hidden="true" fill="none" stroke="#3b3b3b">
      <line x1="160" y1="6" x2="540" y2="6" stroke-width="3"/>
      <line x1="165" y1="15" x2="535" y2="15" stroke-width="2"/>
      <line x1="150" y1="114" x2="530" y2="114" stroke-width="2"/>
      <line x1="155" y1="122" x2="540" y2="122" stroke-width="3"/>
      <line x1="135" y1="38" x2="135" y2="96" stroke-width="3"/>
      <line x1="143" y1="44" x2="143" y2="90" stroke-width="2"/>
      <line x1="552" y1="38" x2="552" y2="96" stroke-width="3"/>
      <line x1="544" y1="44" x2="544" y2="90" stroke-width="2"/>
      <circle cx="546" cy="122" r="4" fill="#3b3b3b" stroke="none"/>
    </svg>
    <h2 class="product-name">RUM</h2>

    <span class="spec spec--strength">100%</span>
    <span class="spec spec--proof">PROOF</span>
    <svg class="spec-rules" viewBox="0 0 690 24" aria-hidden="true">
      <line x1="180" y1="15" x2="330" y2="15" stroke="#3b3b3b" stroke-width="2"/>
      <line x1="356" y1="15" x2="502" y2="15" stroke="#3b3b3b" stroke-width="2"/>
      <path d="M343 3 L348 14 L343 25 L338 14 Z" fill="none" stroke="#3b3b3b" stroke-width="2"/>
    </svg>
    <span class="spec spec--volume">750 ML.</span>
    <span class="spec spec--abv">ALC. 40%</span>

    <svg class="est-ribbon" viewBox="0 0 250 74" aria-label="Established 2019">
      <path d="M0 16 Q125 -4 250 16 L232 42 L250 68 Q125 48 0 68 L18 42 Z" fill="#3b3b3b"/>
      <text x="125" y="49" text-anchor="middle" font-family="Quicksand, sans-serif" font-size="24" font-weight="500" fill="#e6e6e4" letter-spacing="1">ESTD.&#160;&#160;2019</text>
    </svg>

    <p class="tagline">Custom, handcrafted spirits worthy of those standards<br>and focus on those that believe in living free</p>
  </main>
</body>
</html>
```